KT&V PPT

Take my ugly PowerPoint and make it look slick. Use our company color scheme throughout, embed our logo on a couple slides, pick out a couple of stock photos of smiling people and insert where appropriate, and provide multiple slide templates that we can work from. We are launching a new service that is all about reducing time-to-market for medical device manufacturers so include themes relating to medical device, speed, acceleration, overcoming obstacles, and/or breaking down barriers.

```html
<!DOCTYPE html>
<html lang="en">
<head>
<meta charset="utf-8">
<title>Crestline Medical – Pre-Validated Packaging deck</title>
<link href="https://fonts.googleapis.com/css2?family=Roboto:wght@300;400;500;700&display=swap" rel="stylesheet">
<style>
:root{
  --navy:#1e2a3e;
  --navy-deep:#172234;
  --blue:#1b7db8;
  --blue-mid:#3c93c6;
  --blue-pale:#cfe4ef;
  --ink:#2b2f36;
  --grey:#7c838c;
  --light:#f3f5f7;
  --white:#ffffff;
  --stage-top:#c9ccd1;
  --stage-bot:#e9eaec;
}
*{margin:0;padding:0;box-sizing:border-box}
html,body{width:1200px;height:2659px;overflow:hidden}
body{font-family:"Roboto",Arial,sans-serif;color:var(--ink);
  background:linear-gradient(180deg,var(--stage-top) 0,var(--stage-bot) 740px,#ececee 740px,#ececee 100%);position:relative}
.brand{display:flex;align-items:center;gap:4px;font-weight:400;white-space:nowrap}
.brand .dot{border-radius:50%;background:var(--blue);flex:none}
.hero-brand{position:absolute;left:910px;top:48px;font-size:30px;color:var(--navy)}
.hero-brand .dot{width:28px;height:28px}
.hero{position:absolute;left:250px;top:175px;width:362px;height:203px;transform:scale(1.934);transform-origin:top left;box-shadow:0 2px 6px rgba(0,0,0,.25)}

.slide{position:absolute;width:362px;height:203px;overflow:hidden;background:var(--white)}
.slide.dark{background:linear-gradient(120deg,var(--navy) 0,#2c3a55 100%);color:var(--white)}
.photo{position:absolute;background:linear-gradient(135deg,#c8b3a3,#8d7a70 55%,#d9d3cf)}
.photo.cool{background:linear-gradient(135deg,#9fb2c2,#5f7688 60%,#c7d2da)}
.photo.warm{background:linear-gradient(135deg,#d8a45a,#7b6a55 60%,#c9b9a6)}
.disc{position:absolute;border-radius:50%}

.t-logo{position:absolute;left:32px;top:32px;font-size:17px}
.t-logo .dot{width:14px;height:14px}
.t-title{position:absolute;left:32px;top:80px;font-size:17px;font-weight:700;line-height:1.15}
.t-sub{position:absolute;left:32px;top:130px;font-size:5.6px}
.t-date{position:absolute;left:32px;top:152px;font-size:4px;font-weight:500}
.t-band{position:absolute;left:0;bottom:0;width:100%;height:11px;background:var(--blue);font-size:3.6px;color:var(--white);text-align:center;line-height:11px;font-weight:500}
.t-band::after{content:"";position:absolute;left:0;bottom:0;width:100%;height:3px;background:var(--navy-deep)}
.light .t-logo,.light .t-title{color:var(--navy)}
.light .t-sub,.light .t-date{color:var(--grey)}

.foot{position:absolute;left:10px;right:10px;bottom:4px;height:10px;display:flex;justify-content:space-between;align-items:center}
.foot .brand{font-size:8.5px;color:var(--navy)}
.foot .brand .dot{width:7px;height:7px}
.foot small{font-size:3.4px;color:var(--grey)}
.h{position:absolute;left:0;width:100%;text-align:center;font-size:11px;color:var(--ink)}
.hl{position:absolute;font-size:11px;color:var(--ink);line-height:1.15}
.sub{position:absolute;left:0;width:100%;text-align:center;font-size:6.5px;color:var(--blue)}
.bl{position:absolute;list-style:none;font-size:5.6px;line-height:1.3}
.bl li{padding-left:7px;position:relative;margin-bottom:2px}
.bl li::before{content:"";position:absolute;left:0;top:1.5px;width:4px;height:4px;border-radius:50%;background:var(--blue)}
.bl.tiny{font-size:3.8px}
.bl.tiny li{padding-left:5px;margin-bottom:.5px}
.bl.tiny li::before{width:2.5px;height:2.5px;top:1px;background:var(--grey)}
.ico{position:absolute;width:16px;height:16px;border-radius:50%;background:var(--blue);border:2px solid var(--white);box-shadow:0 0 0 .8px var(--blue)}
.cap{position:absolute;font-size:4.6px;color:var(--blue);text-align:center;font-weight:500}
.chev{position:absolute;height:34px;background:var(--light);clip-path:polygon(0 0,92% 0,100% 50%,92% 100%,0 100%,6% 50%)}
.bar{position:absolute;height:12px;background:var(--blue);color:var(--white);font-size:5px;line-height:12px;padding-left:10px;clip-path:polygon(0 0,96% 0,100% 50%,96% 100%,0 100%)}
.dash{position:absolute;height:0;border-top:.8px dashed #b9c3cc}
.note{position:absolute;font-size:3.8px;color:var(--grey);line-height:1.25}
.card{position:absolute;background:var(--white);border-radius:5px;box-shadow:0 1px 3px rgba(0,0,0,.2)}
.chk{font-size:5px}
</style>
</head>
<body>

<div class="hero-brand brand"><span class="dot"></span>Crestline Medical</div>

<section class="slide dark hero">
  <div class="disc photo" role="img" aria-label="Photo of smiling team members" style="left:220px;top:14px;width:180px;height:180px"></div>
  <div class="t-logo brand"><span class="dot"></span>Crestline Medical</div>
  <h1 class="t-title">Pre-Validated<br>Packaging</h1>
  <p class="t-sub">One and Done | MYTH vs Reality | Packaging Validation</p>
  <p class="t-date">Wednesday, February 1, 2023</p>
  <div class="t-band">© 2023 Crestline Medical, Inc.</div>
</section>

<section class="slide dark" style="left:20px;top:763px">
  <div class="disc photo" role="img" aria-label="Photo of smiling team members" style="left:220px;top:14px;width:180px;height:180px"></div>
  <div class="t-logo brand"><span class="dot"></span>Crestline Medical</div>
  <h2 class="t-title">Pre-Validated<br>Packaging</h2>
  <p class="t-sub">One and Done | MYTH vs Reality | Packaging Validation</p>
  <p class="t-date">Wednesday, February 1, 2023</p>
  <div class="t-band">© 2023 Crestline Medical, Inc.</div>
</section>
<section class="slide light" style="left:413px;top:763px">
  <div class="disc photo" role="img" aria-label="Faded photo of smiling team members" style="left:220px;top:14px;width:180px;height:180px;opacity:.55"></div>
  <div class="t-logo brand"><span class="dot"></span>Crestline Medical</div>
  <h2 class="t-title">Pre-Validated<br>Packaging</h2>
  <p class="t-sub">One and Done | MYTH vs Reality | Packaging Validation</p>
  <p class="t-date">Wednesday, February 1, 2023</p>
  <div class="t-band">© 2023 Crestline Medical, Inc.</div>
</section>
<section class="slide dark" style="left:806px;top:763px">
  <div class="disc photo" role="img" aria-label="Photo of smiling team members" style="left:240px;top:20px;width:160px;height:160px"></div>
  <div class="t-logo brand"><span class="dot"></span>Crestline Medical</div>
  <h2 class="t-title">Pre-Validated<br>Packaging</h2>
  <p class="t-sub">One and Done | MYTH vs Reality | Packaging Validation</p>
  <p class="t-date">Wednesday, February 1, 2023</p>
  <div class="t-band">© 2023 Crestline Medical, Inc.</div>
</section>

<section class="slide light" style="left:20px;top:993px">
  <div class="disc photo" role="img" aria-label="Photo of smiling professional" style="left:225px;top:10px;width:180px;height:180px"></div>
  <div class="t-logo brand"><span class="dot"></span>Crestline Medical</div>
  <h2 class="t-title">Pre-Validated<br>Packaging</h2>
  <p class="t-sub">One and Done | MYTH vs Reality | Packaging Validation</p>
  <p class="t-date">Wednesday, February 1, 2023</p>
  <div class="t-band">© 2023 Crestline Medical, Inc.</div>
</section>
<section class="slide light" style="left:413px;top:993px">
  <div class="disc" style="left:225px;top:10px;width:180px;height:180px;background:var(--blue)"></div>
  <div class="t-logo brand"><span class="dot"></span>Crestline Medical</div>
  <h2 class="t-title">Pre-Validated<br>Packaging</h2>
  <p class="t-sub">One and Done | MYTH vs Reality | Packaging Validation</p>
  <p class="t-date">Wednesday, February 1, 2023</p>
  <div class="t-band">© 2023 Crestline Medical, Inc.</div>
</section>
<section class="slide dark" style="left:806px;top:993px">
  <div class="disc" style="left:225px;top:10px;width:180px;height:180px;background:var(--white)"></div>
  <div class="t-logo brand"><span class="dot"></span>Crestline Medical</div>
  <h2 class="t-title">Pre-Validated<br>Packaging</h2>
  <p class="t-sub">One and Done | MYTH vs Reality | Packaging Validation</p>
  <p class="t-date">Wednesday, February 1, 2023</p>
  <div class="t-band">© 2023 Crestline Medical, Inc.</div>
</section>

<section class="slide light" style="left:20px;top:1223px">
  <div class="disc" style="left:225px;top:10px;width:180px;height:180px;background:var(--blue-pale)"></div>
  <div class="t-logo brand"><span class="dot"></span>Crestline Medical</div>
  <h2 class="t-title">Pre-Validated<br>Packaging</h2>
  <p class="t-sub">One and Done | MYTH vs Reality | Packaging Validation</p>
  <p class="t-date">Wednesday, February 1, 2023</p>
  <div class="t-band">© 2023 Crestline Medical, Inc.</div>
</section>
<section class="slide dark" style="left:413px;top:1223px">
  <div class="disc" style="left:225px;top:10px;width:180px;height:180px;background:#34435c"></div>
  <div class="t-logo brand"><span class="dot"></span>Crestline Medical</div>
  <h2 class="t-title">Pre-Validated<br>Packaging</h2>
  <p class="t-sub">One and Done | MYTH vs Reality | Packaging Validation</p>
  <p class="t-date">Wednesday, February 1, 2023</p>
  <div class="t-band">© 2023 Crestline Medical, Inc.</div>
</section>
<section class="slide" style="left:806px;top:1223px">
  <div style="position:absolute;inset:0 0 100px 0;background:linear-gradient(120deg,var(--navy),#3a5577)"></div>
  <div class="h" style="top:12px;color:var(--white);font-size:9.5px;line-height:1.2">What is required of a fully Validated Sterile Barrier<br>Packaging System?</div>
  <div class="h" style="top:40px;color:var(--white);font-size:6px">Which of these benchmarks can be Pre-Validated?</div>
  <div class="card" style="left:16px;top:78px;width:110px;height:98px"></div>
  <div class="card" style="left:130px;top:78px;width:110px;height:98px"></div>
  <div class="card" style="left:244px;top:78px;width:110px;height:98px"></div>
  <div class="ico" style="left:63px;top:68px"></div><div class="ico" style="left:177px;top:68px"></div><div class="ico" style="left:291px;top:68px"></div>
  <div class="cap" style="left:16px;top:87px;width:110px">Package<br>Design</div>
  <div class="cap" style="left:130px;top:87px;width:110px">Process<br>Validation</div>
  <div class="cap" style="left:244px;top:87px;width:110px">Package Performance<br>Transit Testing</div>
  <ul class="bl tiny" style="left:20px;top:103px;width:104px"><li>Microbial barrier properties</li><li>Sterilization compatibility</li><li>Box, shelf and shipping carton</li><li>Biocompatibility and toxicity</li><li>Compatibility of device and package</li><li>Compatibility with labeling</li></ul>
  <ul class="bl tiny" style="left:134px;top:103px;width:104px"><li>Develop sealing parameters</li><li>Sealer IQ, OQ and PQ</li></ul>
  <ul class="bl tiny" style="left:248px;top:103px;width:104px"><li>Environmental conditioning</li><li>Distribution simulation</li><li>Aging (accelerated &amp; real time)</li><li>Aseptic presentation</li></ul>
  <div class="foot"><span class="brand"><span class="dot"></span>Crestline Medical</span><small>© 2023 Crestline Medical, Inc. | 9</small></div>
</section>

<section class="slide" style="left:20px;top:1453px">
  <div class="hl" style="left:20px;top:28px">What's available currently on<br>the <b>"Pre-Validated"</b> market?</div>
  <ul class="bl" style="left:20px;top:70px;width:160px"><li>Generic sterile barrier systems</li><li>Accelerated aging</li><li>Compatible with various sterilization modalities.</li><li>Sealer Validations</li><li>Packaging Materials in stock</li></ul>
  <div class="photo warm" role="img" aria-label="Photo of hands sealing a cardboard box with tape" style="left:195px;top:0;width:160px;height:170px"></div>
  <div class="foot"><span class="brand"><span class="dot"></span>Crestline Medical</span><small>© 2023 Crestline Medical, Inc. | 10</small></div>
</section>
<section class="slide" style="left:413px;top:1453px">
  <div class="photo cool" role="img" aria-label="Photo of a lab technician at a seal testing machine" style="left:20px;top:0;width:84px;height:170px"></div>
  <div class="hl" style="left:116px;top:12px;font-size:10px">Pre-Validated really means<br><b>"Partially Validated"</b>.</div>
  <div class="hl" style="left:116px;top:38px;font-size:7px;color:var(--blue)">What is still required?</div>
  <ul class="bl" style="left:116px;top:82px;width:110px;font-size:4.6px;color:var(--blue)"><li>Distribution testing<ul class="bl tiny" style="position:static;color:var(--grey)"><li>Environmental conditioning</li><li>Distribution simulation</li><li>Sterile barrier testing</li></ul></li><li>Sterilization validation</li><li>Device-specific requirements:<ul class="bl tiny" style="position:static;color:var(--grey)"><li>Accelerated aging</li><li>Real-time aging</li><li>Label design</li></ul></li></ul>
  <ul class="bl" style="left:238px;top:82px;width:112px;font-size:4.6px;color:var(--blue)"><li>Missing critical components of a "World-Class" packaging system:<ul class="bl tiny" style="position:static;color:var(--grey)"><li>Label abrasion test</li><li>Human factors testing</li><li>Documentation of process risk assessment</li><li>Preconfigured shipping carton</li><li>Submission-ready data set</li></ul></li></ul>
  <div class="foot"><span class="brand"><span class="dot"></span>Crestline Medical</span><small>© 2023 Crestline Medical, Inc. | 11</small></div>
</section>
<section class="slide" style="left:806px;top:1453px">
  <div class="h" style="top:12px">How is The Timeline Affected?</div>
  <div class="sub" style="top:42px">Traditional Packaging Validations take 26 – 30 weeks to complete</div>
  <div class="dash" style="left:0;right:0;top:70px"></div>
  <div class="chev" style="left:8px;top:80px;width:88px"></div><div class="chev" style="left:94px;top:80px;width:88px"></div><div class="chev" style="left:180px;top:80px;width:88px"></div><div class="chev" style="left:266px;top:80px;width:88px"></div>
  <div class="ico" style="left:44px;top:62px"></div><div class="ico" style="left:130px;top:62px"></div><div class="ico" style="left:216px;top:62px"></div><div class="ico" style="left:302px;top:62px"></div>
  <div class="cap" style="left:8px;top:83px;width:88px">Package Design</div><div class="cap" style="left:94px;top:83px;width:88px">Process Validation</div><div class="cap" style="left:180px;top:83px;width:88px">Stability Studies</div><div class="cap" style="left:266px;top:83px;width:88px">Distribution Studies</div>
  <ul class="bl tiny" style="left:30px;top:92px"><li>Sterile barrier</li><li>Packaging System</li><li>Labeling</li></ul>
  <ul class="bl tiny" style="left:114px;top:92px"><li>Sealer settings</li><li>OQ, PQ</li></ul>
  <ul class="bl tiny" style="left:198px;top:92px"><li>Real time aging</li></ul>
  <ul class="bl tiny" style="left:282px;top:92px"><li>Environmental conditioning</li><li>Transit simulation</li></ul>
  <div class="bar" style="left:22px;top:142px;width:170px"><span class="chk">✓</span> Pre-Validated &nbsp;&nbsp;&nbsp;&nbsp;&nbsp;&nbsp;&nbsp;&nbsp;&nbsp;&nbsp;&nbsp;&nbsp;&nbsp; <span class="chk">✓</span> Pre-Validated</div>
  <p class="note" style="left:22px;top:159px">Currently available Pre-Validated packaging eliminates<br>10 to 12 of those weeks</p>
  <div class="foot"><span class="brand"><span class="dot"></span>Crestline Medical</span><small>© 2023 Crestline Medical, Inc. | 12</small></div>
</section>

<section class="slide" style="left:20px;top:1683px">
  <div class="h" style="top:12px">Potential Failures</div>
  <div class="photo warm" role="img" aria-label="Photo of warehouse workers handling shipping boxes" style="left:0;top:34px;width:362px;height:64px"></div>
  <div class="ico" style="left:52px;top:104px"></div>
  <div class="chev" style="left:22px;top:122px;width:80px;height:30px"></div>
  <div class="cap" style="left:22px;top:126px;width:62px">Distribution Studies</div>
  <ul class="bl tiny" style="left:34px;top:136px"><li>Environmental conditioning</li><li>Transit simulation</li></ul>
  <div class="cap" style="left:150px;top:112px;width:100px;text-align:left;font-weight:400">Packages can fail in a variety of ways</div>
  <div style="position:absolute;left:156px;top:128px;width:14px;height:14px;background:var(--blue)"></div><span class="cap" style="left:177px;top:132px;color:var(--ink)">Product Damage</span>
  <div style="position:absolute;left:256px;top:128px;width:14px;height:14px;background:var(--blue)"></div><span class="cap" style="left:278px;top:132px;color:var(--ink)">Void</span>
  <div style="position:absolute;left:156px;top:152px;width:14px;height:14px;background:var(--blue)"></div><span class="cap" style="left:177px;top:156px;color:var(--ink)">Puncture</span>
  <div style="position:absolute;left:256px;top:152px;width:14px;height:14px;background:var(--blue)"></div><span class="cap" style="left:278px;top:156px;color:var(--ink)">Creep</span>
  <div class="foot"><span class="brand"><span class="dot"></span>Crestline Medical</span><small>© 2023 Crestline Medical, Inc. | 13</small></div>
</section>
<section class="slide" style="left:413px;top:1683px">
  <div class="hl" style="left:20px;top:22px">Cautionary Advice</div>
  <ul class="bl" style="left:20px;top:52px;width:160px;font-size:5px"><li>Consider packaging EARLY in product development</li><li>Concurrent packaging validation and sterilization validation has risk</li><li><b>Package too large</b> – allows too much movement, pouch material folds are asking for sterile breach (pin holes)</li><li><b>Aging studies:</b> With or without product? Air is easy to validate, but what about product interactions and affects of geometries? World Class studies include the device.</li></ul>
  <div class="photo" role="img" aria-label="Photo of a smiling group of coworkers giving thumbs up" style="left:195px;top:0;width:157px;height:170px"></div>
  <div class="foot"><span class="brand"><span class="dot"></span>Crestline Medical</span><small>© 2023 Crestline Medical, Inc. | 14</small></div>
</section>
<section class="slide" style="left:806px;top:1683px">
  <div class="h" style="top:12px">Let us introduce you to an alternative TRAK</div>
  <div style="position:absolute;left:0;top:34px;width:362px;height:130px;background:linear-gradient(180deg,#eef3f7,#cfe0ec)"></div>
  <div style="position:absolute;left:104px;top:36px;height:100px;border-left:1px solid var(--navy)"></div>
  <div style="position:absolute;left:208px;top:36px;height:100px;border-left:1px solid var(--navy)"></div>
  <div class="cap" style="left:0;top:38px;width:104px;color:var(--navy);font-size:6.5px;font-weight:700">PLANNING</div>
  <div class="cap" style="left:104px;top:38px;width:104px;color:var(--navy);font-size:6.5px;font-weight:700">DEVELOPMENT</div>
  <div class="cap" style="left:208px;top:38px;width:104px;color:var(--navy);font-size:6.5px;font-weight:700">PACKAGING</div>
  <div role="img" aria-label="Illustrated winding road through planning, development and packaging milestones to FDA submission" style="position:absolute;left:10px;top:52px;width:340px;height:80px;background:linear-gradient(160deg,transparent 20%,rgba(27,125,184,.35) 45%,rgba(120,70,160,.3) 60%,transparent 80%)"></div>
  <div style="position:absolute;left:0;top:136px;width:362px;height:18px;background:var(--blue);color:var(--white);font-size:6.5px;text-align:center;line-height:18px">TRAK tm is your complete packaging solution.</div>
  <div class="foot"><span class="brand"><span class="dot"></span>Crestline Medical</span><small>© 2023 Crestline Medical, Inc. | 15</small></div>
</section>

<section class="slide" style="left:20px;top:1913px">
  <div class="hl" style="left:20px;top:14px">The TRAK Difference</div>
  <div class="hl" style="left:20px;top:54px;font-size:5.6px;color:var(--blue);font-weight:500">A Worst Case Proxy Device &amp; More...</div>
  <div class="hl" style="left:20px;top:86px;font-size:5.6px;color:var(--blue)">ISO 11607-1:2019 Speaks to a "Worst-Case".</div>
  <ul class="bl tiny" style="left:20px;top:97px;width:170px;font-size:4.2px"><li>Its built into the TRAK Program</li><li>Has something for everyone (plate, screw, trocar, etc.)</li></ul>
  <p class="note" style="left:20px;top:125px;width:160px;font-size:4.4px;color:var(--ink)">TRAK provides a worst case proxy device to create an Engineering rationale for adoption.</p>
  <div class="photo cool" role="img" aria-label="Photo of a metal proxy medical device" style="left:195px;top:0;width:160px;height:100px;background:linear-gradient(135deg,#f4f4f4,#d8d8d8)"></div>
  <div style="position:absolute;left:195px;top:100px;width:160px;height:70px;background:var(--blue);color:var(--white);font-size:5.2px;padding:10px 12px">Built With:
    <div style="display:grid;grid-template-columns:1fr 1fr;gap:3px 8px;margin-top:8px;font-size:4.4px"><span>• Co-Cr</span><span>• UHMW PE</span><span>• Titanium</span><span>• PEEK</span><span>• Tantalum</span><span>• Additive simulation</span></div></div>
  <div class="foot"><span class="brand"><span class="dot"></span>Crestline Medical</span><small>© 2023 Crestline Medical, Inc. | 16</small></div>
</section>
<section class="slide" style="left:413px;top:1913px">
  <div class="h" style="top:12px">The TRAK Level OF ACCELERATION</div>
  <div style="position:absolute;left:0;top:34px;width:362px;height:12px;background:var(--blue)"></div>
  <div style="position:absolute;left:150px;top:36px;width:50px;height:8px;background:var(--navy);color:var(--white);font-size:3.8px;text-align:center;line-height:8px">2 to 4 Weeks</div>
  <span class="note" style="left:210px;top:38px;color:var(--white)">TRAK Submission Finish</span>
  <div class="dash" style="left:0;right:0;top:70px"></div>
  <div class="ico" style="left:37px;top:62px"></div><div class="ico" style="left:104px;top:62px"></div><div class="ico" style="left:171px;top:62px"></div><div class="ico" style="left:238px;top:62px"></div><div class="ico" style="left:305px;top:62px"></div>
  <div class="cap" style="left:10px;top:82px;width:70px">Package Design</div><div class="cap" style="left:77px;top:82px;width:70px">Process<br>Validation</div><div class="cap" style="left:144px;top:82px;width:70px">Distribution &amp;<br>Aging testing</div><div class="cap" style="left:211px;top:82px;width:70px">Human Factors</div><div class="cap" style="left:278px;top:82px;width:70px">Product Rationale</div>
  <ul class="bl tiny" style="left:22px;top:100px;width:56px"><li>Double sterile barrier system</li><li>Box and labeling</li><li>Qualified supplier</li></ul>
  <ul class="bl tiny" style="left:90px;top:100px;width:56px"><li>Sealer settings validated</li><li>IQ, OQ, PQ for sealer</li><li>Process risk analysis</li></ul>
  <ul class="bl tiny" style="left:157px;top:100px;width:56px"><li>Environmental conditioning</li><li>Distribution simulation</li><li>Accelerated aging</li><li>Label abrasion test</li></ul>
  <ul class="bl tiny" style="left:224px;top:100px;width:56px"><li>Human factors / aseptic presentation study</li></ul>
  <ul class="bl tiny" style="left:291px;top:100px;width:60px"><li>OEM responsibility</li><li>Engineering rationale for adoption</li><li>Drop and vibration results</li></ul>
  <div style="position:absolute;left:90px;top:160px;width:80px;height:9px;background:var(--navy);color:var(--white);font-size:3.8px;text-align:center;line-height:9px">Adds 10 – 12 weeks</div>
  <span class="note" style="left:178px;top:162px">Std. "Pre-Validated" Submission Finish</span>
  <div class="foot"><span class="brand"><span class="dot"></span>Crestline Medical</span><small>© 2023 Crestline Medical, Inc. | 17</small></div>
</section>
<section class="slide" style="left:806px;top:1913px">
  <div class="h" style="top:12px">Time to submission-ready document set</div>
  <div class="photo cool" role="img" aria-label="Photo of hands passing a clipped document" style="left:0;top:34px;width:362px;height:64px;background:linear-gradient(135deg,#6d8296,#c8d2da 60%,#eef1f4)"></div>
  <div style="position:absolute;left:8px;top:102px;width:346px;font-size:4.6px">
    <div style="display:grid;grid-template-columns:90px 22px 1fr;border-bottom:.6px solid #ccc;color:var(--grey);font-size:3.4px"><span>Task Name</span><span>Duration</span><span>1 &nbsp;2 &nbsp;3 &nbsp;4 &nbsp;5 &nbsp;6 &nbsp;7 &nbsp;8 &nbsp;9 &nbsp;10 &nbsp;11 &nbsp;12 &nbsp;13 &nbsp;14 &nbsp;15 &nbsp;16</span></div>
    <div style="display:grid;grid-template-columns:90px 22px 1fr;align-items:center;height:9px"><span>TRAK</span><span>3 wks</span><span style="display:block;height:3px;width:8%;background:var(--blue-mid)"></span></div>
    <div style="display:grid;grid-template-columns:90px 22px 1fr;align-items:center;height:9px"><span>"Pre-Validated"</span><span>12 wks</span><span style="display:block;height:3px;width:35%;background:var(--blue-mid)"></span></div>
    <div style="display:grid;grid-template-columns:90px 22px 1fr;align-items:center;height:9px"><span>Custom Packaging Validation</span><span>30 wks</span><span style="display:block;height:3px;width:90%;background:var(--blue-mid)"></span></div>
  </div>
  <div class="foot"><span class="brand"><span class="dot"></span>Crestline Medical</span><small>© 2023 Crestline Medical, Inc. | 18</small></div>
</section>

<section class="slide" style="left:20px;top:2143px">
  <div class="h" style="top:12px">How is the timeline compressed?</div>
  <div class="sub" style="top:42px">Traditional Packaging Validations take 26 – 30 weeks to complete</div>
  <div class="dash" style="left:0;right:0;top:70px"></div>
  <div class="chev" style="left:8px;top:80px;width:88px"></div><div class="chev" style="left:94px;top:80px;width:88px"></div><div class="chev" style="left:180px;top:80px;width:88px"></div><div class="chev" style="left:266px;top:80px;width:88px"></div>
  <div class="ico" style="left:44px;top:62px"></div><div class="ico" style="left:130px;top:62px"></div><div class="ico" style="left:216px;top:62px"></div><div class="ico" style="left:302px;top:62px"></div>
  <div class="cap" style="left:8px;top:83px;width:88px">Custom Package Design</div><div class="cap" style="left:94px;top:83px;width:88px">Process Validation</div><div class="cap" style="left:180px;top:83px;width:88px">Distribution Testing</div><div class="cap" style="left:266px;top:83px;width:88px">Aging Studies</div>
  <ul class="bl tiny" style="left:30px;top:92px"><li>Sterile barrier</li><li>Packaging System</li><li>Labeling</li></ul>
  <ul class="bl tiny" style="left:114px;top:92px"><li>Sealer settings</li><li>OQ, PQ</li></ul>
  <ul class="bl tiny" style="left:198px;top:92px"><li>Environmental conditioning</li><li>Distribution simulation</li></ul>
  <ul class="bl tiny" style="left:282px;top:92px"><li>Accelerated</li><li>Real Time</li></ul>
  <div class="bar" style="left:22px;top:142px;width:330px;word-spacing:1px"><span class="chk">✓</span> True-Validated &nbsp;&nbsp;&nbsp;&nbsp;&nbsp;&nbsp;&nbsp;&nbsp;&nbsp;&nbsp;&nbsp;&nbsp;&nbsp;&nbsp; <span class="chk">✓</span> True-Validated &nbsp;&nbsp;&nbsp;&nbsp;&nbsp;&nbsp;&nbsp;&nbsp;&nbsp;&nbsp;&nbsp;&nbsp;&nbsp;&nbsp; <span class="chk">✓</span> True-Validated &nbsp;&nbsp;&nbsp;&nbsp;&nbsp;&nbsp;&nbsp;&nbsp;&nbsp;&nbsp;&nbsp;&nbsp;&nbsp;&nbsp; <span class="chk">✓</span> True-Validated</div>
  <p class="note" style="left:22px;top:160px;width:320px">True-Validated packaging is completely validated including distribution and aging studies. The only remaining task is to write the adoption rationale and submit to the FDA</p>
  <div class="foot"><span class="brand"><span class="dot"></span>Crestline Medical</span><small>© 2023 Crestline Medical, Inc. | 19</small></div>
</section>
<section class="slide" style="left:413px;top:2143px">
  <div style="position:absolute;left:0;top:0;width:362px;height:62px;background:linear-gradient(120deg,var(--navy),#3a5577)"></div>
  <div class="h" style="top:26px;color:var(--white)">What data is provided with TRAK?</div>
  <ul class="bl" style="left:20px;top:82px;width:165px;font-size:4.8px"><li>Package design data (material specs, biocompatibility)</li><li>Label formats</li><li>Proxy Representative Device worst-case characteristics</li><li>Sample size rationale</li><li>Sealing Process PFMEA (with FDA Masterfile Reference included)</li></ul>
  <ul class="bl" style="left:190px;top:82px;width:160px;font-size:4.8px"><li>Distribution Simulation Protocol/Report of test results</li><li>Defined shipper configuration of 4-up carton</li><li>Accelerated Aging test results</li><li>Aseptic Presentation/Human factors test results</li><li>Real device - drop and vibration test results</li><li>Rationale guidance document</li></ul>
  <div class="foot"><span class="brand"><span class="dot"></span>Crestline Medical</span><small>© 2023 Crestline Medical, Inc. | 20</small></div>
</section>
<section class="slide" style="left:806px;top:2143px">
  <div style="position:absolute;left:14px;top:14px;width:334px;height:92px;background:linear-gradient(120deg,rgba(27,125,184,.95),rgba(60,147,198,.8))" role="img" aria-label="Blue tinted photo of a laboratory"></div>
  <div class="hl" style="left:34px;top:30px;color:var(--white)">The TRAK To...</div>
  <p class="note" style="left:34px;top:52px;width:135px;color:var(--white);font-size:4.8px">Crestline Medical has created an alliance partnership with eQMS superstars Brightlane.</p>
  <div style="position:absolute;left:186px;top:72px;width:160px;height:92px;background:var(--white);box-shadow:0 1px 3px rgba(0,0,0,.2)"></div>
  <div style="position:absolute;left:244px;top:84px;width:40px;height:18px;background:var(--blue-pale);border-radius:3px"></div>
  <div style="position:absolute;left:236px;top:112px;width:56px;height:10px;background:var(--blue-pale);border-radius:2px"></div>
  <div style="position:absolute;left:232px;top:130px;width:64px;height:10px;background:#d3ead8;border-radius:2px"></div>
  <p class="note" style="left:34px;top:118px;width:140px;color:var(--ink);font-size:4.8px">By providing a world-class Quality Management System at the front end, and a True-Validated packaging system on the back end, the TRAK to market suddenly happens at FULL THROTTLE!</p>
  <div class="foot"><span class="brand"><span class="dot"></span>Crestline Medical</span><small>© 2023 Crestline Medical, Inc. | 21</small></div>
</section>

<section class="slide dark" style="left:216px;top:2373px">
  <div class="disc" style="left:225px;top:10px;width:180px;height:180px;background:var(--white)"></div>
  <div class="t-logo brand" style="top:76px;font-size:13px"><span class="dot" style="width:11px;height:11px"></span>Crestline Medical</div>
  <p style="position:absolute;left:32px;top:112px;font-size:6px;font-weight:500">Contact Us</p>
  <p style="position:absolute;left:32px;top:128px;font-size:4.4px;line-height:2">☎ (555) 014-7720<br>✉ info@crestlinemed.example<br>◉ https://crestlinemed.example</p>
  <div class="t-band">© 2023 Crestline Medical, Inc.</div>
</section>
<section class="slide dark" style="left:609px;top:2373px">
  <div class="disc" style="left:225px;top:10px;width:180px;height:180px;background:#34435c"></div>
  <div class="t-logo brand" style="top:76px;font-size:13px"><span class="dot" style="width:11px;height:11px"></span>Crestline Medical</div>
  <p style="position:absolute;left:32px;top:112px;font-size:6px;font-weight:500">Contact Us</p>
  <p style="position:absolute;left:32px;top:128px;font-size:4.4px;line-height:2">☎ (555) 014-7720<br>✉ info@crestlinemed.example<br>◉ https://crestlinemed.example</p>
  <div class="t-band">© 2023 Crestline Medical, Inc.</div>
</section>

</body>
</html>
```